Marlow Estates Business Card and Email Signature Design

I am a Homevant and need a business card design with my head shot picture and logo and contact information that can be prepared to be used on my email signature as well. I would like my head shot image background to match the background of the business card. So in other words the background of my head shot should be transparent. I would like the Homevant Logo on there and also PRX and Fair Dwelling Logo. My email address is: ted@marlowestates.example, Phone Number is: 555-014-7391, website: www.marlowestates.example Address: 48207 Quillfern Court Carmel, IN 46033
I also need just the head shot photo with white background in a JPEG file as well so I can upload that picture to my Jobtrellis and Nestavo profiles.

```html
<!DOCTYPE html>
<html lang="en">
<head>
<meta charset="utf-8">
<title>Marlow Estates Business Card</title>
<link href="https://fonts.googleapis.com/css2?family=Roboto:wght@400;500&display=swap" rel="stylesheet">
<style>
  :root {
    --page-bg: #d9d4cd;
    --navy-deep: #0f2238;
    --navy-mid: #1d4468;
    --navy-light: #2c5d86;
    --frost: #d3d9de;
    --frost-edge: #c4ccd3;
    --ring: #121820;
    --text-light: #e8eef4;
    --text-soft: #c9d6e2;
    --link: #e5a9ab;
    --brand: #0f2a48;
    --photo-a: #7a5a4a;
    --photo-b: #3a3330;
  }
  html, body {
    margin: 0;
    width: 1200px;
    height: 969px;
    overflow: hidden;
    background: var(--page-bg);
    font-family: "Roboto", Arial, sans-serif;
  }
  .card {
    position: absolute;
    left: 100px;
    top: 200px;
    width: 1000px;
    height: 570px;
    border-radius: 28px;
    overflow: hidden;
    background: var(--frost-edge);
    box-shadow: 0 10px 30px rgba(0,0,0,0.2);
  }
  .navy-field {
    position: absolute;
    left: 0;
    top: 0;
    width: 720px;
    height: 100%;
    background: radial-gradient(ellipse at 35% 30%, var(--navy-light) 0%, var(--navy-mid) 40%, var(--navy-deep) 100%);
  }
  .frost-circle {
    position: absolute;
    left: 418px;
    top: -15px;
    width: 600px;
    height: 600px;
    box-sizing: border-box;
    border-radius: 50%;
    border: 5px solid var(--ring);
    background: radial-gradient(circle at 45% 45%, var(--frost) 0%, var(--frost-edge) 100%);
  }
  .headshot {
    position: absolute;
    left: 79px;
    top: 65px;
    width: 113px;
    height: 147px;
    border: 2px solid #6d8196;
    border-radius: 4px;
    background: linear-gradient(160deg, var(--photo-a), var(--photo-b));
  }
  .name {
    position: absolute;
    left: 226px;
    top: 102px;
    margin: 0;
    font-size: 28px;
    font-weight: 500;
    color: var(--text-light);
  }
  .role {
    position: absolute;
    left: 226px;
    top: 142px;
    margin: 0;
    font-size: 21px;
    font-weight: 400;
    color: var(--text-light);
  }
  .address {
    position: absolute;
    left: 64px;
    top: 330px;
    margin: 0;
    font-size: 24px;
    line-height: 30px;
    color: var(--text-soft);
    font-style: normal;
  }
  .contacts {
    position: absolute;
    left: 64px;
    top: 410px;
    margin: 0;
    padding: 0;
    list-style: none;
    font-size: 23px;
    line-height: 32px;
    color: var(--text-soft);
  }
  .contacts li { display: flex; align-items: center; gap: 12px; }
  .contacts svg { width: 18px; height: 18px; fill: var(--text-soft); }
  .contacts .web { color: var(--link); }
  .brand {
    position: absolute;
    left: 500px;
    top: 165px;
    width: 440px;
    text-align: center;
  }
  .brand-dot {
    width: 126px;
    height: 126px;
    border-radius: 50%;
    background: var(--brand);
    margin: 0 auto 16px;
  }
  .brand-name {
    margin: 0;
    font-size: 38px;
    font-weight: 500;
    color: var(--brand);
    text-transform: uppercase;
  }
</style>
</head>
<body>
  <div class="card">
    <div class="navy-field"></div>
    <div class="frost-circle"></div>

    <div class="headshot" role="img" aria-label="Head shot portrait of Owen Hartley"></div>
    <h1 class="name">OWEN HARTLEY</h1>
    <p class="role">CEO/FOUNDER</p>

    <address class="address">48207 Quillfern<br>Court Carmel, IN 46033</address>

    <ul class="contacts">
      <li>
        <svg viewBox="0 0 24 24" aria-hidden="true"><path d="M6.6 10.8a15.1 15.1 0 0 0 6.6 6.6l2.2-2.2c.3-.3.7-.4 1-.2 1.1.4 2.3.6 3.6.6.6 0 1 .4 1 1V20c0 .6-.4 1-1 1A17 17 0 0 1 3 4c0-.6.4-1 1-1h3.5c.6 0 1 .4 1 1 0 1.3.2 2.5.6 3.6.1.3 0 .7-.2 1z"/></svg>
        555-014-7391
      </li>
      <li>
        <svg viewBox="0 0 24 24" aria-hidden="true"><path d="M2 5h20v2l-10 7L2 7z"/><path d="M2 8l10 7 10-7v11H2z"/></svg>
        ted@marlowestates.example
      </li>
      <li class="web">
        <svg viewBox="0 0 24 24" aria-hidden="true"><path d="M12 2a10 10 0 1 0 0 20 10 10 0 0 0 0-20zm6.9 6h-3a15 15 0 0 0-1.3-3.9A8 8 0 0 1 18.9 8zM12 4c.8 1.2 1.5 2.5 1.9 4h-3.8c.4-1.5 1.1-2.8 1.9-4zM4.3 14a8 8 0 0 1 0-4h3.4a16 16 0 0 0 0 4zm.8 2h3a15 15 0 0 0 1.3 3.9A8 8 0 0 1 5.1 16zm3-8h-3a8 8 0 0 1 4.3-3.9C8.8 5.3 8.4 6.6 8.1 8zM12 20c-.8-1.2-1.5-2.5-1.9-4h3.8c-.4 1.5-1.1 2.8-1.9 4zm2.3-6H9.7a14 14 0 0 1 0-4h4.6a14 14 0 0 1 0 4zm.3 5.9c.6-1.2 1-2.5 1.3-3.9h3a8 8 0 0 1-4.3 3.9zm1.7-5.9a16 16 0 0 0 0-4h3.4a8 8 0 0 1 0 4z"/></svg>
        www.marlowestates.example
      </li>
    </ul>

    <div class="brand">
      <div class="brand-dot"></div>
      <p class="brand-name">Marlow Estates</p>
    </div>
  </div>
</body>
</html>
```